Oil and Gas Exploration and Production company needs a business card design

We need a business card design using our logo and colors in the logo. We want a mainstream design.

```html
<!DOCTYPE html>
<html lang="en">
<head>
<meta charset="utf-8">
<title>Corvane Energy – Business Card</title>
<link href="https://fonts.googleapis.com/css2?family=Arimo:wght@400;700&display=swap" rel="stylesheet">
<style>
  :root {
    --gold: #c9ab2e;
    --ink: #111111;
    --ink-soft: #3a3a3a;
    --paper: #ffffff;
    --rule: #e3e3e3;
    --stage: #e6e4df;
  }
  html, body {
    margin: 0;
    padding: 0;
    width: 1200px;
    height: 1023px;
    overflow: hidden;
    background: var(--stage);
    font-family: "Arimo", Arial, sans-serif;
  }
  .card {
    position: absolute;
    left: 75px;
    top: 211px;
    width: 1050px;
    height: 600px;
    background: var(--paper);
    overflow: hidden;
    box-shadow: 0 10px 30px rgba(0,0,0,0.18);
  }
  .top-band {
    position: absolute;
    left: 0; top: 0;
    width: 100%;
    height: 72px;
    background: var(--gold);
    border-bottom: 8px solid var(--ink);
  }
  .tagline {
    position: absolute;
    left: 34px; top: 20px;
    font-size: 31px;
    color: var(--ink-soft);
    white-space: nowrap;
  }
  .top-stripes {
    position: absolute;
    right: 0; top: 0;
    width: 140px; height: 72px;
  }
  .rig-illustration {
    position: absolute;
    left: 0; top: 150px;
    width: 470px; height: 364px;
    background: linear-gradient(180deg, #2a2a2a 0%, #111 70%, #555 100%);
  }
  .brand {
    position: absolute;
    left: 492px; top: 158px;
    display: flex;
    align-items: center;
    gap: 16px;
    white-space: nowrap;
  }
  .brand-dot {
    width: 40px; height: 40px;
    border-radius: 50%;
    background: var(--ink-soft);
    flex: none;
  }
  .brand-name {
    font-size: 62px;
    line-height: 1;
    font-weight: 700;
    color: var(--ink);
    letter-spacing: -1px;
  }
  .contact-band {
    position: absolute;
    left: 470px; top: 270px;
    width: 580px; height: 210px;
    background: var(--ink);
    color: var(--paper);
  }
  .person-name {
    position: absolute;
    left: 30px; top: 26px;
    font-size: 42px;
    letter-spacing: 0.5px;
    white-space: nowrap;
  }
  .person-title {
    position: absolute;
    left: 32px; top: 82px;
    font-size: 19px;
    white-space: nowrap;
  }
  .address {
    position: absolute;
    left: 32px; top: 138px;
    font-size: 20px;
    display: flex;
    align-items: center;
    gap: 10px;
    white-space: nowrap;
  }
  .bottom-band {
    position: absolute;
    left: 0; bottom: 0;
    width: 100%;
    height: 70px;
    background: var(--gold);
    border-top: 16px solid var(--rule);
  }
  .web {
    position: absolute;
    left: 30px; top: 17px;
    display: flex;
    align-items: center;
    gap: 14px;
    font-size: 32px;
    color: var(--ink);
    white-space: nowrap;
  }
</style>
</head>
<body>
  <div class="card">
    <div class="top-band">
      <span class="tagline">Exploration and Production company</span>
      <svg class="top-stripes" viewBox="0 0 140 72" aria-hidden="true">
        <polygon points="40,72 70,0 84,0 54,72" fill="#ffffff"/>
        <polygon points="68,72 98,0 112,0 82,72" fill="#ffffff"/>
        <polygon points="96,72 126,0 140,0 110,72" fill="#ffffff"/>
      </svg>
    </div>

    <div class="rig-illustration" role="img" aria-label="Black silhouette of an oil pumpjack and oilfield equipment"></div>

    <div class="brand">
      <span class="brand-dot"></span>
      <span class="brand-name">Corvane Energy</span>
    </div>

    <div class="contact-band">
      <div class="person-name">DALE HOLLISTER</div>
      <div class="person-title">President for Northmark Exploration, Inc.</div>
      <div class="address">
        <svg width="16" height="22" viewBox="0 0 16 22" aria-hidden="true">
          <path d="M8 0C3.6 0 0 3.5 0 7.9 0 13.5 8 22 8 22s8-8.5 8-14.1C16 3.5 12.4 0 8 0z" fill="#ffffff"/>
          <circle cx="8" cy="8" r="3" fill="#111111"/>
        </svg>
        <span>2480 Cedar Bend Road Midland, TX 79701</span>
      </div>
    </div>

    <div class="bottom-band">
      <div class="web">
        <svg width="34" height="34" viewBox="0 0 34 34" aria-hidden="true">
          <g fill="none" stroke="#111" stroke-width="2.4">
            <circle cx="17" cy="17" r="14"/>
            <ellipse cx="17" cy="17" rx="6" ry="14"/>
            <line x1="3" y1="17" x2="31" y2="17"/>
            <line x1="6" y1="10" x2="28" y2="10"/>
            <line x1="6" y1="24" x2="28" y2="24"/>
          </g>
        </svg>
        <span>https://www.corvaneenergy.com</span>
      </div>
    </div>
  </div>
</body>
</html>
```